A website for a green bio-plastics manufacturing company

We need a home page designed and two complimentary template pages that can be used for the rest of the website. The template page should vary in design from the home page, but should flow uniformly with it.

This is a very innovative company with a proprietary manufacturing method of using bird feathers to make plastic.

The site should be functional, informative, user-friendly and informative to both our business partners and the consumers.
Updates

I've added a more concise overview of the company.  If any of the designers have any questions for me, please ask.  Thanks

Felix

Target Market(s)

Business partners interested in using bio-plastics for their products and general customers.

Industry/Entity Type

Manufacturing

Number of Pages Required

3 pages

Requirements
Must have
• I attached some information about the company, so the site should be designed to incorporate that content.

Will need to be edited by Adobe Contribute.

Easy to navigate

One of the template pages should have one column for content. The other should have two columns. I''m open to different ideas though.

Should be very pleasing to the eye and uncluttered.

Want to be informative to both our business partners as well as consumers who may be researching our product(s)

Easy to Maintain

Anticipated Tabs/Pages
· Home Page
o General “welcome” page

· About Us
o Company overview and information

· Products
o Horticulture Containers
o Agriculture Films
o Where to Buy
o Upcoming Products

· Business Partners

· Press Releases

· Contact Us

Nice to have
• Would like to have earth tones and or nice greens in the color scheme. They make use of bird feathers for their manufacturing process, so perhaps a real sharp image of a feather can be incorporated into the design. Be creative though.

Perhaps a jQuery nav bar, but that may be out of scope.

Should not have
• No flash at all.

```html
<!DOCTYPE html>
<html lang="en">
<head>
<meta charset="utf-8">
<title>Northfield BioResins – Home</title>
<link href="https://fonts.googleapis.com/css2?family=Jost:wght@400;500;600&family=Noto+Sans:wght@400;700&display=swap" rel="stylesheet">
<style>
  :root {
    --lime: #abc82b;
    --panel: #10110b;
    --panel-edge: #4a4a42;
    --box-top: #1a1b15;
    --box-bottom: #24251f;
    --box-edge: #35362f;
    --olive-head: #9cb52c;
    --text: #f2f2ea;
    --tab: #7a9a06;
    --brand-dot: #2f8a47;
  }
  * { margin: 0; padding: 0; box-sizing: border-box; }
  html, body { width: 1200px; height: 1086px; overflow: hidden; }
  body { background: var(--lime); font-family: "Noto Sans", sans-serif; color: var(--text); position: relative; }

  .site-panel {
    position: absolute; left: 108px; top: 30px; width: 986px; height: 998px;
    background: var(--panel); border: 3px solid var(--panel-edge); border-radius: 14px;
  }

  .main-nav { position: absolute; left: 179px; top: 70px; height: 43px; display: flex; align-items: center;
    font-family: "Jost", sans-serif; font-weight: 500; font-size: 17px; color: #fff; text-transform: uppercase; }
  .main-nav a { color: #fff; text-decoration: none; }
  .main-nav .sep { margin: 0 5px; }
  .main-nav .current { background: var(--tab); padding: 0 6px; height: 43px; line-height: 43px; border-radius: 6px 6px 0 0; margin-right: 10px; }

  .hero { position: absolute; left: 91px; top: 113px; width: 1026px; height: 297px; border-radius: 10px; overflow: hidden; }
  .hero-art { position: absolute; inset: 0;
    background: linear-gradient(135deg, #7fa20a 0%, #9cc413 45%, #8fb80f 75%, #77980a 100%); }
  .brand { position: absolute; left: 42px; top: 88px; display: flex; align-items: center; gap: 16px;
    font-family: "Jost", sans-serif; font-weight: 600; color: #fff; }
  .brand-dot { width: 70px; height: 70px; border-radius: 50%; background: var(--brand-dot); }
  .brand-name { font-size: 38px; line-height: 40px; text-transform: uppercase; }
  .brand-rule { position: absolute; left: 53px; top: 181px; width: 377px; height: 2px; background: #fff; }
  .tagline { position: absolute; left: 508px; top: 174px; font-size: 40px; color: #fff;
    text-shadow: 2px 2px 3px rgba(0,0,0,.35); white-space: nowrap; }

  .section-title { font-family: "Jost", sans-serif; font-weight: 400; font-size: 31px; text-transform: uppercase; line-height: 1; }
  .side-title { color: #fff; }
  .main-title { color: var(--olive-head); }

  .side { position: absolute; left: 124px; width: 300px; }
  .side .section-title { margin-bottom: 10px; padding-left: 3px; }
  .info-box { background: linear-gradient(180deg, var(--box-top), var(--box-bottom)); border: 1px solid var(--box-edge); padding: 8px 10px; font-size: 13px; line-height: 16px; }
  .press-box { height: 173px; position: relative; }
  .press-box p + p { margin-top: 16px; }
  .more { position: absolute; right: 20px; bottom: 8px; font-weight: 700; font-size: 12px; color: #fff; text-decoration: underline; }
  .contact-box { height: 173px; }
  .contact-box h4 { font-size: 13px; font-weight: 700; letter-spacing: 1px; text-transform: uppercase; }
  .contact-box p { margin-bottom: 16px; }

  .main { position: absolute; left: 450px; width: 620px; font-size: 13px; line-height: 19px; letter-spacing: .4px; }
  .main .section-title { margin-bottom: 8px; letter-spacing: 0; }
  .main p { padding-left: 5px; }
  .main p + p { margin-top: 19px; }

  .footer-nav { position: absolute; top: 1052px; left: 391px; display: flex; gap: 16px; font-size: 15px; }
  .footer-nav a { color: #fff; text-decoration: none; text-transform: uppercase; }
</style>
</head>
<body>
  <div class="site-panel"></div>

  <nav class="main-nav">
    <a class="current" href="#">Home Page</a>
    <a href="#">About Us</a><span class="sep">|</span>
    <a href="#">Product Catalogue</a><span class="sep">|</span>
    <a href="#">Business Partners</a><span class="sep">|</span>
    <a href="#">Press Release</a><span class="sep">|</span>
    <a href="#">Contact Us</a>
  </nav>

  <header class="hero">
    <div class="hero-art" role="img" aria-label="Green banner artwork with flowing curves and a green feather"></div>
    <div class="brand">
      <span class="brand-dot"></span>
      <span class="brand-name">Northfield<br>Bio Resins</span>
    </div>
    <div class="brand-rule"></div>
    <div class="tagline">Customers are "Partners"</div>
  </header>

  <aside class="side" style="top:463px">
    <h2 class="section-title side-title">Press Release</h2>
    <div class="info-box press-box">
      <p>Lorem Ipsum is simply dummy text of the printing and typesetting industry. Lorem Ipsum has been the industry's standard dummy text ever since the 1500s,</p>
      <p>Lorem Ipsum is simply dummy text of the printing and typesetting industry.</p>
      <a class="more" href="#">More</a>
    </div>
  </aside>

  <aside class="side" style="top:740px">
    <h2 class="section-title side-title">Contact Us</h2>
    <div class="info-box contact-box">
      <h4>Head Office</h4>
      <p>42 alder row<br>greenford, midshire, gf2 7pl.</p>
      <h4>E-mail</h4>
      <p>info@northfieldbio.com</p>
      <h4>Contact</h4>
      <p>Landline: 111 4820 617<br>Fax: 111 4820 640</p>
    </div>
  </aside>

  <section class="main" style="top:463px">
    <h1 class="section-title main-title">Wel Come</h1>
    <p>Northfield BioResins is a green-technology start-up company that has implemented cutting edge technology and custom-designed machines to manufacture bioplastics from poultry feathers on an industrial scale. Danny Felix, who brings a wealth of experience in agriculture, poultry, and business, is the entrepreneur behind the company’s creation and development.</p>
    <p>Northfield BioResins plans to manufacture virgin keratin-based resins and both sell these resins and further compound them to meet desired specifications. We plan to sell manufactured and compounded resins to our business partners who will further process these resins into end user products such as: greenhouse/nursery containers, agricultural</p>
  </section>

  <section class="main" style="top:748px">
    <h2 class="section-title main-title">Our Vision</h2>
    <p>Become the leading manufacturer and distributor of bioplastics in the world.</p>
  </section>

  <section class="main" style="top:835px">
    <h2 class="section-title main-title">Our Mission</h2>
    <p>Engineer, implement and perfect processes and formulations to cost-effectively convert poultry feathers into bioplastics that meet the specific needs of local, national and international agricultural and consumer markets.</p>
  </section>

  <footer class="footer-nav">
    <a href="#">Home</a><a href="#">Product</a><a href="#">Partners</a><a href="#">Contact Us</a>
  </footer>
</body>
</html>
```